Cinco de Mayo Event Poster- Los Cerritos

I need a poster for our restaurant, Los Cerritos, for Cinco de Mayo.
Final Size 11"x17"(portrait).
Use our official Los Cerritos Logo.
Date: Tuesday May 5
Live Music/ Mariachi/ DJ/ Ice Luge/ Beer Tent/ Giveaways.
Include our phone number 555-418-2936
Address : 47116 Garnet Rd, Livonia, MI 48150
website : www.loscerritoskitchen-demo.com

Industry/Entity Type

Restaurant

Colors
0054AA
0677BA
7BADD7
CADEEF
E8F1F8
0094D4
00A9DD
6FCCEA
C7EBF8
E9F6FB
00AB8E
00BBA5
67D7C9
C6EFE9
E9F9F6
FFC000
F8CF3A
FAE287
FDF2CF
FEFAEE
EE7325
F08F49
F5BC92
FAE3D3
FDF4ED
E54698
E96AAD
F1A4CE
F9D9EA
FCEFF6
A7469A
B969AE
D3A5CF
EDDBEB
F8F0F9
6B429C
8869AF
B7A5CE
E3DAEB
F3F0F8

Requirements
Must have
• Vereda Tequila Logo, Lumbral Tequila Logo.
Nice to have
• Palm Trees, margaritas, Mexican beer. I added our menus to give you a better Idea of who we are.vd
Should not have
• maracas/sombreros

```html
<!DOCTYPE html>
<html lang="en">
<head>
<meta charset="utf-8">
<title>Los Cerritos – Cinco de Mayo</title>
<link rel="stylesheet" href="https://fonts.googleapis.com/css2?family=Outfit:wght@500;600;800;900&display=swap">
<style>
  :root {
    --night: #1c0a3f;
    --night-top: #2a1655;
    --gold: #ffc000;
    --gold-light: #f8cf3a;
    --orange: #ee7325;
    --pink: #e54698;
    --teal: #00bba5;
    --ink: #2b1c24;
    --white: #ffffff;
  }
  * { margin: 0; padding: 0; box-sizing: border-box; }
  html, body { width: 776px; height: 1200px; overflow: hidden; background: var(--night); }
  .poster {
    position: relative; width: 776px; height: 1200px; overflow: hidden;
    background: linear-gradient(var(--night-top) 0 318px, var(--night) 318px);
    font-family: "Outfit", sans-serif; color: var(--white);
  }
  .festive-garland {
    position: absolute; left: 0; top: 0; width: 776px; height: 130px;
    background: linear-gradient(180deg, rgba(238,115,37,.55), rgba(229,70,152,.35) 45%, rgba(0,187,165,.18) 75%, rgba(42,22,85,0));
  }
  .brand { position: absolute; left: 0; top: 168px; width: 776px; text-align: center; }
  .brand-name {
    font-weight: 800; font-size: 66px; line-height: 1; color: var(--orange); letter-spacing: 1px;
  }
  .brand-tagline {
    margin-top: 14px; font-weight: 600; font-size: 22px; letter-spacing: 3px; text-transform: uppercase; color: var(--white);
  }
  .title-ornament {
    position: absolute; left: 170px; width: 436px; height: 40px; border-radius: 20px;
    background: linear-gradient(90deg, rgba(0,187,165,.45), rgba(238,115,37,.5) 50%, rgba(229,70,152,.45));
  }
  .title-ornament.top { top: 360px; }
  .title-ornament.bottom { top: 500px; left: 150px; width: 476px; height: 34px; }
  .event-title {
    position: absolute; left: 0; top: 412px; width: 776px;
    display: flex; justify-content: center; align-items: center; gap: 22px;
    font-weight: 900; text-transform: uppercase; line-height: 1;
  }
  .event-title .word { font-size: 84px; color: var(--gold); letter-spacing: 2px; }
  .event-title .joiner { font-size: 28px; color: var(--white); font-weight: 800; margin-top: 18px; }
  .event-date {
    position: absolute; left: 0; top: 578px; width: 776px; text-align: center;
    font-weight: 500; font-size: 42px; line-height: 1;
  }
  .highlights { position: absolute; left: 62px; top: 669px; width: 652px; height: 112px; }
  .highlights svg { position: absolute; inset: 0; }
  .highlights-text {
    position: absolute; inset: 0; display: flex; flex-direction: column; justify-content: center; align-items: center;
    font-weight: 800; font-size: 22.5px; line-height: 1.45; color: var(--ink); text-transform: uppercase;
  }
  .drinks-photo {
    position: absolute; left: 0; top: 786px; width: 776px; height: 268px;
    background: radial-gradient(ellipse at 50% 40%, rgba(240,143,73,.5), rgba(107,66,156,.45) 55%, rgba(28,10,63,.9)),
                linear-gradient(180deg, #2e1d4a, #5a3a2c 70%, #2a1a30);
  }
  .sponsors { position: absolute; left: 0; top: 1054px; width: 500px; height: 146px; }
  .sponsor-primary {
    position: absolute; left: 60px; top: 50px; width: 240px; text-align: center;
    font-weight: 800; font-size: 34px; line-height: 1.1; color: var(--gold-light); letter-spacing: 1px;
  }
  .sponsor-secondary {
    position: absolute; left: 330px; top: 12px; width: 110px; text-align: center;
    font-weight: 800; font-size: 22px; color: var(--white);
  }
  .sponsor-secondary .dot {
    display: block; width: 76px; height: 76px; margin: 10px auto 0; border-radius: 50%; background: var(--white);
  }
  .contact {
    position: absolute; left: 455px; top: 1078px; width: 306px; text-align: center;
    font-style: normal; font-weight: 500; font-size: 18.5px; line-height: 25px;
  }
  .contact-line { display: flex; justify-content: center; align-items: center; gap: 7px; }
  .contact-line svg { flex: none; }
  .contact-web { margin-top: 2px; font-size: 17px; }
</style>
</head>
<body>
<main class="poster">
  <div class="festive-garland" role="img" aria-label="Colourful papel picado bunting and paper flowers"></div>

  <header class="brand">
    <div class="brand-name">Los Cerritos</div>
    <div class="brand-tagline">Authentic Mexican Restaurant</div>
  </header>

  <div class="title-ornament top" role="img" aria-label="Festive leaf and flourish decoration"></div>
  <h1 class="event-title">
    <span class="word">Cinco</span>
    <span class="joiner">de</span>
    <span class="word">Mayo</span>
  </h1>
  <div class="title-ornament bottom" role="img" aria-label="Chili peppers and small bunting flags"></div>

  <p class="event-date">Tuesday May 5</p>

  <section class="highlights">
    <svg width="652" height="112" viewBox="0 0 652 112" aria-hidden="true">
      <defs>
        <linearGradient id="ribbonGold" x1="0" y1="0" x2="0" y2="1">
          <stop offset="0" stop-color="#ffc000"/>
          <stop offset="1" stop-color="#f8cf3a"/>
        </linearGradient>
      </defs>
      <path d="M3 3 H649 Q610 56 649 109 H3 Q42 56 3 3 Z" fill="url(#ribbonGold)" stroke="#ffffff" stroke-width="2.5"/>
    </svg>
    <div class="highlights-text">
      <span>Live Music/ Mariachi/ DJ/ Ice Luge</span>
      <span>Beer Tent/ Giveaways</span>
    </div>
  </section>

  <div class="drinks-photo" role="img" aria-label="Row of colourful margaritas and cocktails with citrus garnishes on a wooden table"></div>

  <section class="sponsors">
    <div class="sponsor-primary">Vereda Tequila</div>
    <div class="sponsor-secondary">Lumbral<span class="dot"></span></div>
  </section>

  <address class="contact">
    <div class="contact-line">
      <svg width="18" height="18" viewBox="0 0 24 24" aria-hidden="true"><path fill="#ee7325" d="M6.6 10.8a15.1 15.1 0 0 0 6.6 6.6l2.2-2.2c.3-.3.7-.4 1-.2 1.1.4 2.3.6 3.6.6.6 0 1 .4 1 1V20c0 .6-.4 1-1 1A17 17 0 0 1 3 4c0-.6.4-1 1-1h3.5c.6 0 1 .4 1 1 0 1.3.2 2.5.6 3.6.1.3 0 .7-.2 1z"/></svg>
      <span>555-418-2936</span>
    </div>
    <div class="contact-line">
      <svg width="16" height="20" viewBox="0 0 16 20" aria-hidden="true"><path fill="#ffc000" d="M8 0a8 8 0 0 0-8 8c0 6 8 12 8 12s8-6 8-12a8 8 0 0 0-8-8zm0 11a3 3 0 1 1 0-6 3 3 0 0 1 0 6z"/></svg>
      <span>47116 Garnet Rd, Livonia,</span>
    </div>
    <div>MI 48150</div>
    <div class="contact-line contact-web">
      <svg width="17" height="17" viewBox="0 0 24 24" aria-hidden="true"><g fill="none" stroke="#ee7325" stroke-width="2.4"><circle cx="12" cy="12" r="10"/><path d="M2 12h20M12 2c3 3 3 17 0 20M12 2c-3 3-3 17 0 20"/></g></svg>
      <span>www.loscerritoskitchen-demo.com</span>
    </div>
  </address>
</main>
</body>
</html>
```